Leaflet to promote a new sports massage business

I am a Remedial and Sports Massage therapist and treat a range of people from professionals who spend hours working behind computers and have associated neck and back pain through poor posture to amateur sports people of varying intensity/ability - who encounter injuries along the way, or just need some good old stretching out.Remedial and sports massage helps people who have musculoskeletal injury, pain or dysfunction brought about by the stresses and strains of life. Through massage i can reduce pain, promote recovery after injury, relieve stress, and improve flexibility. All of this contributes to helping people feel better. I have just started working at a new location (address attached) and am looking to raise awareness that I am there and to promote the benefits of massage to encourage new clients(attached as a separate document). I have a business card (attached to the brief) which uses hands as the main device, I would like to include these – possibly in some sort of logo and I would like to use purple as a key colour (if colour is used). I also want to include the KVTB logo (attached) to add credibility

```html
<!DOCTYPE html>
<html lang="en">
<head>
<meta charset="utf-8">
<title>Helena Marsden – Remedial and Sports Massage Leaflet</title>
<link href="https://fonts.googleapis.com/css2?family=Quicksand:wght@400;500;600;700&family=Montserrat:wght@700;800&display=swap" rel="stylesheet">
<style>
  :root {
    --purple-deep: #5b1a61;
    --purple-mid: #7b2d86;
    --purple-ring: #9a3fa3;
    --ink: #2b1d2f;
    --paper: #ffffff;
    --backdrop: #e9e6e2;
    --skin-light: #f3dccb;
    --skin-mid: #d9ab8c;
    --footer-edge: #e4e0e6;
  }
  * { box-sizing: border-box; margin: 0; padding: 0; }
  html, body { width: 1183px; height: 1200px; overflow: hidden; }
  body { background: var(--backdrop); font-family: "Quicksand", sans-serif; color: var(--ink); position: relative; }

  .leaflet {
    position: absolute; left: 41px; top: 211px;
    width: 1100px; height: 778px;
    background: var(--paper);
    overflow: hidden;
    box-shadow: 0 6px 24px rgba(0,0,0,.18);
  }
  .hero-photo {
    position: absolute; left: 380px; top: 0; width: 720px; height: 514px;
    background:
      linear-gradient(to right, var(--paper) 0%, rgba(255,255,255,0) 30%),
      linear-gradient(to bottom, rgba(255,255,255,0) 55%, var(--paper) 100%),
      radial-gradient(ellipse at 60% 40%, var(--skin-light) 0%, var(--skin-mid) 55%, #f1ece8 85%);
  }
  .brand-circle {
    position: absolute; left: 95px; top: 91px; width: 252px; height: 252px;
    border-radius: 50%; border: 5px solid var(--purple-ring);
    background: var(--paper);
  }
  .brand-name {
    position: absolute; left: 33px; top: 346px; width: 390px;
    font-size: 43px; font-weight: 600; color: var(--purple-mid);
    letter-spacing: -0.5px; line-height: 1; white-space: nowrap;
  }
  .brand-role {
    position: absolute; left: 41px; top: 392px;
    font-family: "Montserrat", sans-serif; font-weight: 700; font-style: italic;
    font-size: 12.5px; letter-spacing: 1.6px; color: var(--ink);
  }
  .intro {
    position: absolute; left: 39px; top: 423px; width: 790px;
    font-size: 15px; line-height: 20px; font-weight: 500;
  }
  .intro strong { font-weight: 700; }
  .benefits-title {
    position: absolute; left: 39px; top: 497px;
    font-size: 30px; font-weight: 600; color: var(--purple-mid); letter-spacing: -0.3px;
  }
  .benefit {
    position: absolute; font-size: 17px; font-weight: 500; white-space: nowrap;
    display: flex; align-items: center; gap: 4px;
  }
  .benefit svg { width: 18px; height: 16px; }
  .accent-block {
    position: absolute; left: 1013px; top: 491px; width: 87px; height: 115px;
    background: var(--purple-deep);
  }
  .partner {
    position: absolute; left: 860px; top: 515px;
    display: flex; align-items: center; gap: 12px;
  }
  .partner-dot { width: 40px; height: 40px; border-radius: 50%; background: var(--purple-deep); }
  .partner-name { font-size: 28px; font-weight: 600; color: var(--purple-deep); letter-spacing: 4px; }

  .contact-band {
    position: absolute; left: 0; top: 604px; width: 1100px; height: 158px;
    background: var(--purple-deep); color: var(--paper);
  }
  .footer-edge { position: absolute; left: 0; top: 762px; width: 1100px; height: 16px; background: var(--footer-edge); }
  .announcement {
    position: absolute; left: 0; top: 24px; width: 100%; text-align: center;
    font-family: "Montserrat", sans-serif; font-weight: 800; font-size: 24px; letter-spacing: -0.3px;
  }
  .address-icon { position: absolute; left: 138px; top: 90px; width: 48px; height: 46px; }
  .address {
    position: absolute; left: 196px; top: 62px; font-size: 23px; line-height: 25.5px; font-weight: 500;
  }
  .phone-icon { position: absolute; left: 468px; top: 108px; width: 24px; height: 24px; }
  .phone { position: absolute; left: 497px; top: 104px; font-size: 25px; font-weight: 500; }
  .mail-icon { position: absolute; left: 672px; top: 112px; width: 32px; height: 20px; }
  .email { position: absolute; left: 710px; top: 109px; font-size: 18px; font-weight: 500; }
</style>
</head>
<body>
  <main class="leaflet">
    <div class="hero-photo" role="img" aria-label="Photograph of a relaxed man lying on a massage table receiving a shoulder massage"></div>

    <div class="brand-circle" aria-hidden="true"></div>
    <h1 class="brand-name">HELENA MARSDEN</h1>
    <p class="brand-role">REMEDIAL AND SPORTS MASSAGE THERAPIST</p>

    <p class="intro">Remedial and sports massage helps people who have musculoskeletal injury, pain or dysfunction brought about by the stresses and strains of life. <strong>Through massage I can reduce pain, promote recovery after injury, relieve stress, and improve flexibility.</strong> All of this contributes to helping people feel better.</p>

    <h2 class="benefits-title">BENEFITS OF MASSAGE</h2>
    <div class="benefit" style="left:19px;top:536px"><svg viewBox="0 0 18 16"><path d="M1 9 L6 14 L17 1" fill="none" stroke="#2b1d2f" stroke-width="3"/></svg>Reduces pain</div>
    <div class="benefit" style="left:305px;top:536px"><svg viewBox="0 0 18 16"><path d="M1 9 L6 14 L17 1" fill="none" stroke="#2b1d2f" stroke-width="3"/></svg>Promotes recovery</div>
    <div class="benefit" style="left:19px;top:563px"><svg viewBox="0 0 18 16"><path d="M1 9 L6 14 L17 1" fill="none" stroke="#2b1d2f" stroke-width="3"/></svg>Improves posture and flexibility</div>
    <div class="benefit" style="left:305px;top:563px"><svg viewBox="0 0 18 16"><path d="M1 9 L6 14 L17 1" fill="none" stroke="#2b1d2f" stroke-width="3"/></svg>Relieves stress</div>
    <div class="benefit" style="left:488px;top:563px"><svg viewBox="0 0 18 16"><path d="M1 9 L6 14 L17 1" fill="none" stroke="#2b1d2f" stroke-width="3"/></svg>Improves health and wellbeing</div>

    <div class="accent-block" aria-hidden="true"></div>
    <div class="partner"><span class="partner-dot" aria-hidden="true"></span><span class="partner-name">KVTB</span></div>

    <section class="contact-band">
      <p class="announcement">PERFORMANCE PHYSIOTHERAPY NOW AVIALABLE</p>
      <svg class="address-icon" viewBox="0 0 48 46" aria-hidden="true"><path d="M24 2 L2 22 H8 V44 H20 V32 H28 V44 H40 V22 H46 Z" fill="#3d0f42"/></svg>
      <p class="address">Riverside Athletic Ground<br>Mill Lane Road<br>Eastbrook, EB4 7QT.</p>
      <svg class="phone-icon" viewBox="0 0 24 24" aria-hidden="true"><path d="M6 2 L10 7 L8 10 C9 13 11 15 14 16 L17 14 L22 18 L19 22 C10 21 3 14 2 5 Z" fill="#3d0f42"/></svg>
      <p class="phone">07700 900456</p>
      <svg class="mail-icon" viewBox="0 0 32 20" aria-hidden="true"><rect x="1" y="1" width="30" height="18" fill="#3d0f42"/><path d="M1 1 L16 12 L31 1" fill="none" stroke="#5b1a61" stroke-width="2"/></svg>
      <p class="email">helenamarsden@mail.com</p>
    </section>
    <div class="footer-edge" aria-hidden="true"></div>
  </main>
</body>
</html>
```